label design for our sauces - please note not a flyer - but a LABEL for a jam & sauce jar
I have attached a sample of a few done by a friend. They are ok but I want something more please.
I am looking for it to be a bit sharper, font like the logo and some separation of the areas on the sides of the labels. Lines or dots or something.
I do also want to consider adding a piece of fruit as either a nice image or a stock line drawing. Id like a few options please? we have in total 12 labels we need asap and then we will want about another 12 after that.
See our competitors that we are trying to take inspiration from.
https://www.fallowmere.com.au - see particularly their strawberry jam label
also see https://www.tilvanes.com.au as a smaple of a nice whaite label but We want the trees to be a color as well as the top and bottom band.
Also we want 2 ranges, one with the white label and color on the band and the tree but the rest black text and then a black label with white text and a gold bad and leaves on the tree.
Can you please take these guides and create something please. the size of the labels to print is 60x160
Id like to get something in the next 24 hours if possible as I really need to get this completed this week.....

```html
<!DOCTYPE html>
<html lang="en">
<head>
<meta charset="utf-8">
<title>Hollin's Larder – Pineapple Rum Jam labels</title>
<link rel="stylesheet" href="https://fonts.googleapis.com/css2?family=Oswald:wght@400;500&family=Cinzel:wght@400&display=swap">
<style>
  :root {
    --stage: #d79a36;
    --ink: #1b1b1b;
    --paper: #ffffff;
    --gold: #f2a516;
    --orange: #e2571e;
    --hatch-light: #d9d9d9;
    --hatch-dark: #2a2a2a;
  }
  * { box-sizing: border-box; margin: 0; padding: 0; }
  html, body { width: 1200px; height: 900px; overflow: hidden; }
  body {
    background: var(--stage);
    font-family: "Oswald", "Arial Narrow", sans-serif;
    position: relative;
  }
  .label {
    position: absolute;
    top: 230px;
    width: 440px;
    height: 440px;
    overflow: hidden;
  }
  .label--black { left: 120px; --bg: var(--ink); --fg: var(--paper); --accent: var(--gold); --hatch: var(--hatch-light); --pattern: #3a3a3a; }
  .label--white { left: 640px; --bg: var(--paper); --fg: var(--ink); --accent: var(--orange); --hatch: var(--hatch-dark); --pattern: #f3e3d8; }

  .label__pattern {
    position: absolute; inset: 0;
    background: linear-gradient(135deg, var(--bg) 0%, var(--pattern) 50%, var(--bg) 100%);
  }
  .label__band {
    position: absolute; top: 0; left: 195px;
    width: 50px; height: 90px;
    background: var(--accent);
  }
  .badge {
    position: absolute; top: 56px; left: 107px;
    width: 226px; height: 330px;
    color: var(--fg);
    text-align: center;
  }
  .badge__shape { position: absolute; inset: 0; }
  .badge__row { position: absolute; left: 0; right: 0; }

  .brand__mark {
    top: 20px; left: 100px; right: auto;
    width: 26px; height: 26px; border-radius: 50%;
    background: var(--accent);
  }
  .brand__name {
    top: 62px; font-size: 23px; font-weight: 500; line-height: 28px;
    color: var(--accent); letter-spacing: 0.3px;
  }
  .label--white .brand__name { color: var(--fg); }
  .brand__tagline {
    top: 92px; font-family: "Cinzel", serif; font-size: 7.5px;
    letter-spacing: 0.8px; line-height: 10px;
  }
  .rule {
    left: 14px; right: 14px; height: 0;
    border-top: 2px dotted var(--accent);
  }
  .rule--1 { top: 108px; }
  .rule--2 { top: 152px; }
  .rule--3 { top: 222px; }
  .product__name {
    top: 113px; font-size: 25px; font-weight: 500; line-height: 36px;
    color: var(--accent);
  }
  .claims {
    top: 158px; height: 60px; display: flex; padding: 0 12px;
  }
  .claim {
    font-size: 19px; line-height: 28px; text-align: left;
  }
  .claim--natural { flex: 1.6; }
  .claim--gluten { flex: 1; padding-left: 8px; border-left: 2px dotted var(--fg); }
  .weight {
    top: 229px; height: 32px; display: flex; align-items: center;
    gap: 8px; padding: 0 14px;
  }
  .weight__hatch { flex: 1; height: 26px; background: var(--hatch); opacity: 0.85; }
  .weight__value { font-size: 22px; line-height: 30px; }
  .est {
    top: 268px; font-size: 14px; line-height: 20px;
  }
  .est__star { top: 290px; height: 14px; }
</style>
</head>
<body>

  <section class="label label--black" aria-label="Black range label">
    <div class="label__pattern" role="img" aria-label="Repeating white sketched pineapple pattern on black"></div>
    <div class="label__band"></div>
    <div class="badge">
      <svg class="badge__shape" viewBox="0 0 226 330" aria-hidden="true">
        <path d="M0,50 H60 Q70,50 78,40 Q113,0 148,40 Q156,50 166,50 H226 V290 H171 Q151,290 141,305 Q113,340 85,305 Q75,290 55,290 H0 Z" fill="var(--bg)"/>
        <path d="M8,58 H60 Q72,58 80,48 Q113,12 146,48 Q154,58 166,58 H218 V282 H171 Q149,282 139,297 Q113,330 87,297 Q77,282 55,282 H8 Z" fill="none" stroke="var(--accent)" stroke-width="1.5"/>
      </svg>
      <div class="badge__row brand__mark"></div>
      <div class="badge__row brand__name">HOLLIN'S LARDER</div>
      <div class="badge__row brand__tagline">PROUDLY AUSTRALIAN SINCE 1987</div>
      <div class="badge__row rule rule--1"></div>
      <div class="badge__row product__name">PINEAPPLE RUM JAM</div>
      <div class="badge__row rule rule--2"></div>
      <div class="badge__row claims">
        <div class="claim claim--natural">ALL NATURAL<br>INGREDIENTS</div>
        <div class="claim claim--gluten">GLUTEN<br>FREE</div>
      </div>
      <div class="badge__row rule rule--3"></div>
      <div class="badge__row weight">
        <div class="weight__hatch" role="img" aria-label="Sketched hatching"></div>
        <div class="weight__value">215g</div>
        <div class="weight__hatch" role="img" aria-label="Sketched hatching"></div>
      </div>
      <div class="badge__row est">EST 1987</div>
      <svg class="badge__row est__star" viewBox="0 0 226 14" aria-hidden="true">
        <polygon points="113,1 115,6 120,6 116,9 118,14 113,11 108,14 110,9 106,6 111,6" fill="var(--fg)"/>
      </svg>
    </div>
  </section>

  <section class="label label--white" aria-label="White range label">
    <div class="label__pattern" role="img" aria-label="Repeating orange and black sketched pineapple pattern on white"></div>
    <div class="label__band"></div>
    <div class="badge">
      <svg class="badge__shape" viewBox="0 0 226 330" aria-hidden="true">
        <path d="M0,50 H60 Q70,50 78,40 Q113,0 148,40 Q156,50 166,50 H226 V290 H171 Q151,290 141,305 Q113,340 85,305 Q75,290 55,290 H0 Z" fill="var(--bg)"/>
        <path d="M8,58 H60 Q72,58 80,48 Q113,12 146,48 Q154,58 166,58 H218 V282 H171 Q149,282 139,297 Q113,330 87,297 Q77,282 55,282 H8 Z" fill="none" stroke="var(--accent)" stroke-width="1.5"/>
      </svg>
      <div class="badge__row brand__mark"></div>
      <div class="badge__row brand__name">HOLLIN'S LARDER</div>
      <div class="badge__row brand__tagline">PROUDLY AUSTRALIAN SINCE 1987</div>
      <div class="badge__row rule rule--1"></div>
      <div class="badge__row product__name">PINEAPPLE RUM JAM</div>
      <div class="badge__row rule rule--2"></div>
      <div class="badge__row claims">
        <div class="claim claim--natural">ALL NATURAL<br>INGREDIENTS</div>
        <div class="claim claim--gluten">GLUTEN<br>FREE</div>
      </div>
      <div class="badge__row rule rule--3"></div>
      <div class="badge__row weight">
        <div class="weight__hatch" role="img" aria-label="Sketched hatching"></div>
        <div class="weight__value">215g</div>
        <div class="weight__hatch" role="img" aria-label="Sketched hatching"></div>
      </div>
      <div class="badge__row est">EST 1987</div>
      <svg class="badge__row est__star" viewBox="0 0 226 14" aria-hidden="true">
        <polygon points="113,1 115,6 120,6 116,9 118,14 113,11 108,14 110,9 106,6 111,6" fill="var(--fg)"/>
      </svg>
    </div>
  </section>

</body>
</html>
```